依頼詳細
ダイナミックなチラシとポスターをお願いします。
見ただけで「すごい!講演に行ってみたい!!」と思えるような。
記載項目
添付資料のとおり
サイズ
A2ポスターとA4チラシ
ページ数
片面
希望イメージ
シンプル 複雑
単色 カラフル
暗い 明るい
日常 高級
遊び心 厳粛
未来的 伝統的
女性的 男性的
納品ファイル
• 高解像度JPG (.jpg)
• イラストレーター形式 (.ai)
補足説明
開催内容の資料を送ります。
また、講師のプロフィールを送ります。

クレジットは、写真提供:森川拓事務所もしくは(c)Taku Morikawa Office等とご表記ください。
皆様お世話になっております。

ポスターの写真は、スポンサーの関係で前回添付した画像以外は基本的には、使用ができませんのでご了承ください。
そのほかの写真を使いたい場合は、一度こちらに確認いただきます様よろしくお願いします。
皆様いつもお世話になっております。
画像が添付されておりませんでした。大変失礼しました。

ご対応どうぞよろしくお願いします。
左上にPRVマークをつけていただきます様よろしくお願いします。
なお、空白とマークの位置はデータのバランスを維持していただきます様お願いします。
■ 選んだ理由

全体の色合いも非常によかったです。ダイナミックな雰囲気と仲間の絆のイメージをうまく表現していただけたと思います。

■ 提案者全員のお礼・コメント

皆様、たくさんのご応募ありがとうございました。こちらのイメージをうまく呼んでいただいたかと思います。
次回もどうぞよろしくお願いします。

```html
<!DOCTYPE html>
<html lang="ja">
<head>
<meta charset="utf-8">
<title>仲間の絆 森川拓 講演</title>
<link href="https://fonts.googleapis.com/css2?family=Noto+Sans+JP:wght@400;700;900&family=Shippori+Mincho+B1:wght@800&display=swap" rel="stylesheet">
<style>
:root{
  --sky-top:#12306e;
  --sky-low:#5f86c4;
  --snow:#e8eef6;
  --band:#2f8fd8;
  --band-light:#8fd0f5;
  --ice-top:#cfe7f5;
  --ice-low:#8dbad8;
  --navy:#0d2f6b;
  --blue:#1565c0;
  --ink:#111;
  --white:#fff;
  --paper:#f4f8fb;
}
*{margin:0;padding:0;box-sizing:border-box}
html,body{width:853px;height:1200px;overflow:hidden;background:var(--paper)}
.poster{position:relative;width:853px;height:1200px;overflow:hidden;font-family:"Noto Sans JP",sans-serif;color:var(--ink)}
.hero-photo{position:absolute;left:0;top:0;width:853px;height:640px;
  background:linear-gradient(180deg,var(--sky-top) 0%,#2a4f95 40%,var(--sky-low) 70%,var(--snow) 100%)}
.ice-photo{position:absolute;left:0;top:620px;width:853px;height:580px;
  background:linear-gradient(180deg,var(--ice-top) 0%,#b5d7ec 45%,var(--ice-low) 100%)}
.name-band{position:absolute;left:0;top:0;width:853px;height:1200px}
.brand{position:absolute;left:22px;top:20px;display:flex;align-items:center;gap:8px;
  font-weight:900;font-size:26px;color:var(--white);letter-spacing:1px}
.brand-dot{width:20px;height:20px;border-radius:50%;background:var(--white)}
.title{position:absolute;right:18px;top:18px;writing-mode:vertical-rl;
  font-family:"Shippori Mincho B1",serif;font-weight:800;font-size:150px;line-height:1;
  color:var(--white);letter-spacing:4px;text-shadow:0 3px 10px rgba(0,0,0,.35)}
.subtitle{position:absolute;right:178px;top:70px;writing-mode:vertical-rl;
  font-family:"Shippori Mincho B1",serif;font-weight:800;font-size:34px;color:var(--white);
  letter-spacing:3px;text-shadow:0 2px 6px rgba(0,0,0,.4)}
.speaker{position:absolute;left:18px;top:575px;transform:rotate(-9deg);transform-origin:left top;
  display:flex;align-items:flex-end;gap:14px}
.speaker-name{font-weight:900;font-size:150px;line-height:1;color:var(--white);letter-spacing:10px;
  -webkit-text-stroke:4px var(--navy);paint-order:stroke fill}
.speaker-kind{writing-mode:vertical-rl;font-weight:900;font-size:44px;color:var(--white);
  -webkit-text-stroke:2px var(--navy);paint-order:stroke fill;margin-bottom:8px}
.schedule{position:absolute;left:40px;top:800px;display:flex;align-items:flex-end;gap:6px;color:var(--blue)}
.year{font-weight:700;font-size:24px;writing-mode:vertical-rl;margin-bottom:10px}
.date{font-weight:900;font-size:104px;line-height:.9;letter-spacing:-2px}
.weekday{font-weight:900;font-size:38px;margin-bottom:6px}
.time{position:absolute;left:372px;top:806px;background:var(--ink);color:var(--white);
  padding:4px 14px;font-weight:900;font-size:38px;line-height:1.2}
.doors{position:absolute;left:372px;top:862px;font-weight:700;font-size:28px;color:var(--ink)}
.free{position:absolute;left:650px;top:812px;font-weight:900;font-size:32px;color:var(--blue)}
.venue{position:absolute;left:30px;top:905px;font-weight:900;font-size:44px;color:var(--navy);letter-spacing:2px}
.ticket-info{position:absolute;left:260px;top:968px;width:370px;font-size:16px;line-height:1.45;font-weight:700;color:var(--ink)}
.portrait{position:absolute;left:655px;top:960px;width:170px;height:125px;
  background:linear-gradient(180deg,#c9ced6,#6f7a8a)}
.profile{position:absolute;left:470px;top:1095px;width:355px;font-size:10px;line-height:1.5;color:var(--ink)}
.notes{position:absolute;left:250px;top:1090px;width:210px;font-size:10px;line-height:1.5;color:var(--ink)}
</style>
</head>
<body>
<main class="poster">
  <div class="hero-photo" role="img" aria-label="雪山を背景にニット帽とゴーグルを着けた登山家の写真"></div>
  <div class="ice-photo" role="img" aria-label="青白い氷河の氷壁と小さく写る登山者の写真"></div>

  <svg class="name-band" viewBox="0 0 853 1200" aria-hidden="true">
    <defs>
      <linearGradient id="bandFill" x1="0" y1="0" x2="1" y2="1">
        <stop offset="0" stop-color="#1f6fc0"/>
        <stop offset=".55" stop-color="#3aa0e4"/>
        <stop offset="1" stop-color="#8fd0f5"/>
      </linearGradient>
    </defs>
    <polygon points="0,590 853,450 853,640 0,790" fill="url(#bandFill)" opacity=".92"/>
  </svg>

  <div class="brand"><span class="brand-dot"></span>PRV</div>

  <h1 class="title">仲間の絆</h1>
  <p class="subtitle">〜夢と希望に向かって〜</p>

  <div class="speaker">
    <span class="speaker-name">森川拓</span>
    <span class="speaker-kind">講演</span>
  </div>

  <div class="schedule">
    <span class="year">2013</span>
    <span class="date">7.14</span>
    <span class="weekday">(日)</span>
  </div>
  <div class="time">14:00～16:30</div>
  <div class="doors">(開場 13:00)</div>
  <div class="free">入場無料</div>

  <p class="venue">桜台市西部市民会館ホール</p>

  <p class="ticket-info">一般社団法人 桜台青年会議所 事務局<br>〒000-0000 桜台市本町4丁目2番1号 TEL 0120-45-6789<br>にて、入場整理券をお配りしております。</p>

  <div class="portrait" role="img" aria-label="講師のポートレート写真"></div>

  <p class="notes">整理券配布期間 6月1日(月)〜6月28日(金)<br>平日9時〜17時 定員になり次第終了となります。</p>
  <p class="profile">森川拓 登山家。世界各地の高峰に挑み、山の清掃活動や環境教育にも取り組む。全国で講演を続け、夢を持ち続ける大切さを伝えている。写真提供:森川拓事務所</p>
</main>
</body>
</html>
```